Startup FinTech / Behavioural Science company needs website redesign

We are a startup company interested in redesigning our website. We have most of our content created already (viewable at www.tallowmint.example), but are interested in an upgraded look and feel. We are happy to adjust content as well based on design input. We will move hosting from brixelpad to hostvarra or similar hosting service, so portability of files is important to us. Our team will have the ability to make minor tweaks/content adjustments, but would look to engage with someone for more-comprehensive enhancements in the future.
Updates

Reason: Other business needs prevented me from providing timely feedback. I will work on feedback over the next two days but wanted to give additional time for design submissions and revisions.

Target Market(s)

Financial advisors in the US and UK, as well as potential end-users of the tools and potential investors

Industry/Entity Type

Information Technology

Coding

Coded - Design and coding required

Number of Pages Required

1 page

Font styles to use
Sans Serif

Requirements
Must have
• - Lighter, cleaner look and feel. We believe our current website is too heavy and "angular."
• - improved iconography to convey behavioural finance concepts (e.g., herd mentality, and illusion of control)
• - links to social media sites
• - integration with our brixelpad personality profile (viewable now at https://lenaobisk.formquill.example/to/qZ7mRt. Note: we will change this URL to tallowmint.formquill.example... as a part of the design process)
Nice to have
• - ability for us to add a tab/link to a blog in the future.
• - design that allows us to add additional
• - ability for us to add additional pages (e.g., results from our personality profiles, pages to customize sharing on social media)
• - simple ability to enter an email address to add to our mailing list/request more info
• - mobile-responsive design
Should not have
• - Should not have items like office directions and maps, since we are a virtual team.
• - Contact information (e.g., phone number) should be lower down the page vs. at the top
• - comments boxes or lengthy web forms. A simple name/email address is sufficient.

```html
<!DOCTYPE html>
<html lang="en">
<head>
<meta charset="utf-8">
<title>tallowmint</title>
<link rel="stylesheet" href="https://fonts.googleapis.com/css2?family=Montserrat:wght@500;600;700&family=Open+Sans:ital,wght@0,400;0,600;0,700;1,400&family=Oswald:wght@300;400;500&display=swap">
<style>
:root{
  --purple:#7a2a8e;
  --purple-dark:#5e1f70;
  --ink:#222228;
  --text:#4a4a50;
  --frame:#e8e8ea;
  --light:#f2f2f4;
  --white:#ffffff;
}
*{box-sizing:border-box;margin:0;padding:0}
html,body{width:1200px;height:3191px;overflow:hidden}
body{background:var(--frame);font-family:"Open Sans",Arial,sans-serif;color:var(--text)}
.page{position:absolute;left:15px;top:17px;width:1170px;height:3158px;background:var(--white)}
section,header,footer{position:relative;width:100%;overflow:hidden}

/* header */
.site-header{height:106px;display:flex;align-items:center;justify-content:space-between;padding:0 30px 0 22px}
.brand{font-family:"Montserrat",sans-serif;font-weight:600;font-size:44px;color:var(--purple);letter-spacing:-.5px}
.nav{display:flex;gap:26px;align-items:flex-end;padding-top:34px}
.nav a{font-family:"Oswald",sans-serif;font-weight:500;font-size:14px;color:var(--ink);text-decoration:none;position:relative;text-transform:uppercase}
.nav a.active{color:var(--purple)}
.nav a.active::before{content:"";position:absolute;left:50%;top:-32px;width:24px;height:24px;margin-left:-12px;border-radius:50%;border:3px solid var(--purple)}

/* hero */
.hero{height:686px;color:var(--white);text-align:center}
.hero-photo{position:absolute;inset:0;background:linear-gradient(160deg,#6f6a64 0%,#4a4540 40%,#7d756a 70%,#5c5a44 100%)}
.hero-photo::after{content:"";position:absolute;inset:0;background:rgba(0,0,0,.25)}
.hero-content{position:relative;padding-top:170px}
.hero h1{font-family:"Oswald",sans-serif;font-weight:300;font-size:56px;letter-spacing:1px;line-height:1}
.hero .rule{width:640px;height:1px;background:rgba(255,255,255,.7);margin:22px auto 26px}
.hero .tagline{display:flex;justify-content:center;align-items:baseline;gap:14px}
.hero .tagline .brand{color:var(--white);font-size:48px}
.hero .tagline span{font-family:"Oswald",sans-serif;font-weight:300;font-size:38px}
.btn{display:inline-block;background:var(--purple);color:var(--white);font-family:"Oswald",sans-serif;font-weight:400;font-size:26px;text-decoration:none;border-radius:4px;border:2px solid rgba(255,255,255,.8)}
.hero .btn{margin-top:24px;width:192px;height:48px;line-height:44px}
.quote-band{position:absolute;left:0;bottom:0;width:100%;height:128px;background:linear-gradient(#2b2b2b,#1b1b1b);text-align:center;padding-top:24px}
.quote-band q{font-style:italic;font-size:17px;color:#d9d9d9}
.quote-band cite{display:block;font-style:normal;font-family:"Oswald",sans-serif;font-size:28px;color:#cfcfcf;letter-spacing:1px;margin-top:6px}

/* section titles */
.section-title{display:flex;align-items:center;justify-content:center;gap:14px;font-family:"Montserrat",sans-serif;font-weight:700;font-size:26px;color:var(--ink)}
.section-title::before,.section-title::after{content:"";width:110px;height:1px;background:#bdbdc2}
.section-title .dot{width:30px;height:30px;border-radius:50%;border:3px solid var(--purple)}
.section-title em{font-style:normal;color:var(--purple)}
.section-title .brand{font-size:26px}

/* problem */
.problem{height:489px}
.problem .section-title{margin-top:76px;width:800px}
.problem-copy{position:absolute;left:60px;top:150px;width:680px;font-size:14.5px;line-height:1.55;color:#3d3d42}
.problem-copy p{margin-bottom:20px}
.problem-art{position:absolute;left:795px;top:80px;width:300px;height:352px;border-radius:8px;background:linear-gradient(160deg,#e7d6ea 0%,#d9b98c 45%,#c99a62 70%,#2f6f78 100%);opacity:.85}

/* why */
.why{height:458px;background:linear-gradient(135deg,#f7f7f8 0%,#ececee 45%,#f5f5f6 70%,#e9e9eb 100%)}
.why .section-title{margin-top:76px}
.why-list{display:flex;justify-content:space-around;width:900px;margin:40px auto 0;list-style:none}
.why-list li{width:180px;text-align:center;font-family:"Montserrat",sans-serif;font-weight:600;font-size:15px;color:var(--ink)}
.icon-circle{width:88px;height:88px;border-radius:50%;background:var(--white);box-shadow:0 2px 8px rgba(0,0,0,.12);margin:0 auto 22px;display:flex;align-items:center;justify-content:center}
.why-close{text-align:center;margin-top:60px;font-family:"Montserrat",sans-serif;font-weight:600;font-size:22px;color:var(--ink)}
.why-close .brand{font-size:26px}

/* solution */
.solution{height:436px}
.solution .section-title{margin-top:88px}
.steps{display:flex;justify-content:space-around;width:1000px;margin:40px auto 0;list-style:none}
.steps li{width:210px;text-align:center;font-size:14px;line-height:1.4;color:#3d3d42}
.steps svg{display:block;margin:0 auto 10px}
.steps h3{font-family:"Montserrat",sans-serif;font-weight:700;font-size:15px;color:var(--ink)}

/* team */
.team{height:553px}
.team-pattern{position:absolute;right:0;top:0;width:640px;height:100%;background:linear-gradient(100deg,#ffffff 0%,#efeff1 35%,#e2e2e5 70%,#f2f2f4 100%)}
.team .section-title{position:relative;margin-top:96px}
.member{position:absolute;top:219px;width:324px;height:324px;border-radius:50%;border:4px solid var(--purple);background:var(--white);overflow:hidden;text-align:center}
.member.ceo{left:238px}
.member.cto{left:610px}
.member h3{background:var(--purple);color:var(--white);font-family:"Oswald",sans-serif;font-weight:400;font-size:24px;height:92px;padding-top:34px}
.member ul{list-style:none;margin-top:20px;font-family:"Montserrat",sans-serif;font-weight:600;font-size:14px;line-height:1.55;color:var(--ink)}

/* take profile */
.take-profile{height:234px}
.take-profile h2{position:absolute;left:60px;top:40px;font-family:"Oswald",sans-serif;font-weight:500;font-size:50px;color:var(--purple);line-height:1}
.take-profile p{position:absolute;left:60px;top:104px;width:480px;white-space:nowrap;font-family:"Open Sans",sans-serif;font-weight:700;font-size:18px;color:var(--purple)}
.take-profile .btn{position:absolute;left:60px;top:150px;width:152px;height:40px;line-height:36px;font-size:20px;text-align:center;border-radius:2px;border:0}
.profile-art{position:absolute;left:560px;top:10px;width:610px;height:224px;background:linear-gradient(90deg,#2a9bb2 0%,#c24a2a 25%,#3a3a40 50%,#c7a41c 75%,#3f6f54 100%);opacity:.85}

/* footer */
.site-footer{height:166px;background:linear-gradient(120deg,var(--purple) 0%,#8b3aa0 50%,var(--purple-dark) 100%);color:var(--white)}
.site-footer .brand{position:absolute;left:124px;top:52px;color:var(--white);font-size:50px}
.contact{position:absolute;top:46px;text-align:center;font-size:15px;line-height:1.4}
.contact.phone{left:500px}
.contact.mail{left:730px}
.contact svg{display:block;margin:0 auto 8px}
.social{position:absolute;left:952px;top:68px;display:flex;gap:4px}
.social span{width:26px;height:26px;border-radius:50%;border:2px solid var(--white)}
.copyright{height:30px;text-align:center;font-size:10px;font-weight:600;color:var(--ink);line-height:30px}
</style>
</head>
<body>
<div class="page">

<header class="site-header">
  <div class="brand">tallowmint</div>
  <nav class="nav">
    <a class="active" href="#home">Home</a>
    <a href="#problem">The Problem</a>
    <a href="#solution">The Solution</a>
    <a href="#team">Our Team</a>
    <a href="#profile">Take Profile</a>
    <a href="#contact">Contact</a>
  </nav>
</header>

<section class="hero" id="home">
  <div class="hero-photo" role="img" aria-label="Photo of a stressed man rubbing his eyes at a desk with a laptop, crumpled paper and a plant"></div>
  <div class="hero-content">
    <h1>MONEY DECISIONS CAN STRESS YOU OUT</h1>
    <div class="rule"></div>
    <div class="tagline"><span class="brand">tallowmint</span><span>can help</span></div>
    <a class="btn" href="#profile">Get Started</a>
  </div>
  <blockquote class="quote-band">
    <q>Once you have ordinary intelligence, what you need is the temperament to control the urges that get other people in to trouble in investing.</q>
    <cite>HARLAN OAKES</cite>
  </blockquote>
</section>

<section class="problem" id="problem">
  <h2 class="section-title"><span class="dot"></span><span>THE <em>PROBLEM</em></span></h2>
  <div class="problem-copy">
    <p>Money and financial issues are the leading causes of anxiety for most of us. This financial stress is among the leading causes of divorce, addiction, obesity and depression.</p>
    <p>What's worse, the consequences of the decisions that we make can make us even more stressed, not more relieved.</p>
    <p>Ask anyone the key to good physical health, and you're likely to get a correct answer: don't overeat, choose healthy foods and exercise regularly. The path to good physical health is not a mystery, but we have a hard time following it.</p>
    <p>Good financial health works the same way. We generally know what to do – spend less than we earn, save for a rainy day, and make non-emotional investment decisions – but have a hard time doing it.</p>
  </div>
  <div class="problem-art" role="img" aria-label="Illustration of a man carrying a heavy box labelled money issues piled with bills and a calculator"></div>
</section>

<section class="why">
  <h2 class="section-title"><span class="dot"></span><span>WHY</span></h2>
  <ul class="why-list">
    <li><div class="icon-circle"><svg width="36" height="44" viewBox="0 0 36 44"><path d="M18 3a13 13 0 0 0-8 23c2 2 3 4 3 6h10c0-2 1-4 3-6A13 13 0 0 0 18 3z" fill="none" stroke="var(--purple)" stroke-width="3"/><rect x="12" y="35" width="12" height="3" fill="var(--purple)"/><rect x="14" y="40" width="8" height="3" fill="var(--purple)"/></svg></div>Short-term Thinking</li>
    <li><div class="icon-circle"><svg width="50" height="40" viewBox="0 0 50 40"><circle cx="25" cy="10" r="7" fill="var(--purple)"/><circle cx="10" cy="14" r="6" fill="var(--purple)"/><circle cx="40" cy="14" r="6" fill="var(--purple)"/><path d="M13 38c0-10 5-16 12-16s12 6 12 16z" fill="var(--purple)"/><path d="M0 38c0-8 4-13 10-13 3 0 5 1 6 3-2 3-3 6-3 10z" fill="var(--purple)"/><path d="M50 38c0-8-4-13-10-13-3 0-5 1-6 3 2 3 3 6 3 10z" fill="var(--purple)"/></svg></div>Herd Mentality</li>
    <li><div class="icon-circle"><svg width="40" height="44" viewBox="0 0 40 44"><rect x="4" y="2" width="22" height="32" rx="2" fill="none" stroke="var(--purple)" stroke-width="2.5"/><rect x="14" y="10" width="22" height="32" rx="2" fill="var(--white)" stroke="var(--purple)" stroke-width="2.5"/><path d="M25 19l5 7-5 7-5-7z" fill="var(--purple)"/></svg></div>Gambler's Fallacy</li>
    <li><div class="icon-circle"><svg width="50" height="32" viewBox="0 0 50 32"><rect x="1" y="2" width="48" height="28" rx="14" fill="var(--purple)"/><rect x="11" y="14" width="12" height="4" fill="#fff"/><rect x="15" y="10" width="4" height="12" fill="#fff"/><circle cx="34" cy="16" r="2.6" fill="#fff"/><circle cx="39" cy="12" r="2.6" fill="#fff"/></svg></div>Illusion of Control</li>
  </ul>
  <p class="why-close">This is where <span class="brand">tallowmint</span> comes in.</p>
</section>

<section class="solution" id="solution">
  <h2 class="section-title"><span class="dot"></span><span>THE <span class="brand">tallowmint</span> <em>SOLUTION</em></span></h2>
  <ul class="steps">
    <li><svg width="70" height="70" viewBox="0 0 70 70"><circle cx="35" cy="35" r="30" fill="none" stroke="var(--purple)" stroke-width="5"/></svg><h3>Take the profile</h3>Take the tallowmint profile to learn more about your financial personality and tendencies</li>
    <li><svg width="70" height="70" viewBox="0 0 70 70"><circle cx="30" cy="30" r="20" fill="none" stroke="var(--purple)" stroke-width="6"/><rect x="27" y="19" width="6" height="22" fill="var(--purple)"/><rect x="19" y="27" width="22" height="6" fill="var(--purple)"/><path d="M44 44l16 16" stroke="var(--purple)" stroke-width="9" stroke-linecap="round"/></svg><h3>Gain better insight</h3>Play the investment simulation to gain better insight into your strengths and weaknesses</li>
    <li><svg width="70" height="70" viewBox="0 0 70 70"><g fill="none" stroke="var(--purple)" stroke-width="7" stroke-linecap="round"><path d="M30 40l-8 8a9 9 0 0 1-13-13l10-10a9 9 0 0 1 13 0"/><path d="M40 30l8-8a9 9 0 0 1 13 13L51 45a9 9 0 0 1-13 0"/><path d="M28 42l14-14"/></g></svg><h3>Connect your accounts</h3>Connect your financial accounts to see your opportunities to be a better saver and investor</li>
    <li><svg width="70" height="70" viewBox="0 0 70 70"><g fill="var(--purple)"><rect x="8" y="48" width="8" height="14"/><rect x="21" y="40" width="8" height="22"/><rect x="34" y="30" width="8" height="32"/><rect x="47" y="18" width="8" height="44"/></g><path d="M8 38L40 14" stroke="var(--purple)" stroke-width="3"/><path d="M34 10l10 2-4 9z" fill="var(--purple)"/></svg><h3>Check your progress</h3>Check your progress over time to stay on track</li>
  </ul>
</section>

<section class="team" id="team">
  <div class="team-pattern" role="img" aria-label="Soft grey hexagon pattern background"></div>
  <h2 class="section-title"><span class="dot"></span><span>OUR <em>TEAM</em></span></h2>
  <article class="member ceo">
    <h3>Lena Obisk, CFA</h3>
    <ul><li>CEO / Head of "Fin"</li><li>FinTech Veteran</li><li>Investment Portfolio Manager</li><li>Westmarch Business School</li><li>Redfield Technical University</li><li>ProNet</li></ul>
  </article>
  <article class="member cto">
    <h3>Marek Dunhill</h3>
    <ul><li>CTO / Head of "Tech"</li><li>Data Science Expert</li><li>Predictive Analytics Solution Architect</li><li>Alderbrook University</li><li>University of Eastvale</li><li>ProNet</li></ul>
  </article>
</section>

<section class="take-profile" id="profile">
  <h2>TAKE PROFILE</h2>
  <p>Want to learn about your financial personality?</p>
  <a class="btn" href="https://tallowmint.formquill.example">Learn More</a>
  <div class="profile-art" role="img" aria-label="Illustration of five people in a row with thought bubbles about money"></div>
</section>

<footer class="site-footer" id="contact">
  <div class="brand">tallowmint</div>
  <div class="contact phone">
    <svg width="26" height="26" viewBox="0 0 26 26"><circle cx="13" cy="13" r="13" fill="#fff"/><path d="M8 7h3l1 4-2 1a8 8 0 0 0 4 4l1-2 4 1v3c-6 1-12-5-11-11z" fill="var(--purple)"/></svg>
    +1 555 014 2287<br>+44 7700 900 431
  </div>
  <div class="contact mail">
    <svg width="26" height="26" viewBox="0 0 26 26"><circle cx="13" cy="13" r="13" fill="#fff"/><rect x="7" y="8" width="12" height="9" fill="none" stroke="var(--purple)" stroke-width="1.6"/><path d="M7 8l6 5 6-5" fill="none" stroke="var(--purple)" stroke-width="1.6"/></svg>
    info@tallowmint.example
  </div>
  <div class="social"><span></span><span></span><span></span></div>
</footer>
<div class="copyright">COPYRIGHT © 2017 TALLOWMINT. ALL RIGHTS RESERVED.</div>

</div>
</body>
</html>
```